Hip / Cool Business Card for Custom Accessory Company

I would like to get a 2 sided design for standard size business cards, glossy (2 inches x 3.5 inches). Can be landscape or portrait layout! The design should include our logo (attached). The card should be extremely clear that the company is Tin Lantern. Should also have our URL clear. Should also use the color scheme seen on our upcoming site, tinlantern.example. The font we use is called "hurry up." Other than that, please go-to-town. We are targeting 15-45 y.o. market, with a skew on the 20-30 crowd. We do custom and stock iPhone cases as well as Cufflinks, Winestoppers; see the website for more.
Updates

Project Deadline Extended
Reason: Extending in case the US July 4th Holiday is keeping people from working!!

Industry/Entity Type

Landscape

Requirements
Must have
• Must be clear that the website is tinlantern.example. Must be clear that custom designs are an option.
Nice to have
• images of our designs. examples of our designs.
Should not have
• hard on the eyes contrasting colors such as orange on black. green on blue. Should not have any fonts that are considered "old" like Times New Roman. But decorative fonts are fine.

```html
<!DOCTYPE html>
<html lang="en">
<head>
<meta charset="utf-8">
<title>Tin Lantern — Business Card</title>
<link rel="stylesheet" href="https://fonts.googleapis.com/css2?family=Questrial&display=swap">
<style>
  :root {
    --page-bg: #eceff1;
    --teal-deep: #0a4352;
    --teal-mid: #127f98;
    --teal-bright: #1fb6da;
    --brand-teal: #2a9aa3;
    --ink: #161616;
    --contact-teal: #1b9fb0;
    --card-white: #ffffff;
    --ghost: #eef0f1;
  }
  * { box-sizing: border-box; margin: 0; padding: 0; }
  html, body { width: 1200px; height: 784px; overflow: hidden; }
  body {
    background: var(--page-bg);
    font-family: "Questrial", "Century Gothic", sans-serif;
  }
  .canvas {
    position: relative;
    width: 1200px;
    height: 784px;
    display: flex;
    align-items: center;
    justify-content: center;
    gap: 40px;
  }
  .card {
    position: relative;
    width: 540px;
    height: 309px;
    overflow: hidden;
    box-shadow: 0 6px 18px rgba(0,0,0,0.15);
  }

  /* Back side */
  .card--back { background: var(--teal-deep); }
  .pattern-field {
    position: absolute; inset: 0;
    background:
      radial-gradient(circle at 88% 30%, rgba(31,182,218,0.95) 0%, rgba(31,182,218,0) 55%),
      radial-gradient(circle at 70% 85%, rgba(31,182,218,0.6) 0%, rgba(31,182,218,0) 45%),
      linear-gradient(115deg, var(--teal-deep) 0%, var(--teal-mid) 50%, var(--teal-bright) 100%);
  }
  .back-brand {
    position: absolute; inset: 0;
    display: flex; flex-direction: column;
    align-items: center; justify-content: center; gap: 12px;
  }
  .brand-dot {
    width: 84px; height: 84px; border-radius: 50%;
    background: var(--brand-teal);
    border: 3px solid var(--card-white);
  }
  .back-brand .brand-name {
    color: var(--card-white);
    font-size: 40px;
    line-height: 1;
    letter-spacing: 2px;
    text-transform: uppercase;
  }
  .back-brand .tagline {
    color: var(--card-white);
    font-size: 16px;
    letter-spacing: 1px;
  }

  /* Front side */
  .card--front { background: var(--card-white); }
  .ghost-circle {
    position: absolute;
    right: -60px; top: 70px;
    width: 230px; height: 230px;
    border-radius: 50%;
    background: var(--ghost);
  }
  .front-brand {
    position: absolute;
    left: 36px; top: 22px;
    width: 170px;
    display: flex; flex-direction: column; align-items: center; gap: 8px;
  }
  .front-brand .brand-dot {
    width: 74px; height: 74px; border: none;
  }
  .front-brand .brand-name {
    color: var(--ink);
    font-size: 28px;
    letter-spacing: 1px;
    text-transform: uppercase;
    text-align: center;
    line-height: 1.05;
  }
  .contact {
    position: absolute;
    left: 36px; bottom: 22px;
    font-style: normal;
    font-size: 17px;
    line-height: 1.4;
    color: var(--contact-teal);
  }
  .contact .site { color: var(--ink); }
</style>
</head>
<body>
  <main class="canvas">
    <section class="card card--back" aria-label="Card back">
      <div class="pattern-field" role="img" aria-label="Teal background with a pattern of overlapping light circles"></div>
      <div class="back-brand">
        <div class="brand-dot"></div>
        <div class="brand-name">Tin Lantern</div>
        <div class="tagline">Custom &amp; stock designs</div>
      </div>
    </section>

    <section class="card card--front" aria-label="Card front">
      <div class="ghost-circle"></div>
      <div class="front-brand">
        <div class="brand-dot"></div>
        <div class="brand-name">Tin<br>Lantern</div>
      </div>
      <address class="contact">
        <div class="site">tinlantern.example</div>
        <div>418B Copper Hollow Lane Suite 27</div>
        <div>Fairbrook, VA 20199</div>
        <div>hello@tinlantern.example</div>
      </address>
    </section>
  </main>
</body>
</html>
```